Industrial Company needing new business cards

We are a newly branded Industrial trade company. We specialise in Electrical, Mechanical and Air-conditioning.

I would like to see designs single sided. Focusing on the color scheme white/red/black and possibly gray. Possibly make it a black card with white writting... but open to all designs.

I would like the design to be professional, sleek and to the point.

Industry/Entity Type

Business

Contact Information for Business Card

Tom Harwell
Managing Director / Electrician
tomwork@vandilo.com.au
417 Calloway Street, Pembrook NSW 2458
Mobile: 0497551832
www.harwellindustrialgroup.com.au

Requirements
Must have
• Must be able to be sent in a manner that i can change the details for each employee.
• Our logo
Nice to have
• Would like it to somehow have " incorporating Barvo Group Pty Ltd" as this is the company we have taken over.
Should not have
• No yellow!!!
• must not simply place "barvo group" randomly on the business card. refer nice to have.

```html
<!DOCTYPE html>
<html lang="en">
<head>
<meta charset="utf-8">
<title>Harwell Industrial Group – Business Card</title>
<link rel="stylesheet" href="https://fonts.googleapis.com/css2?family=Lato:wght@400;700;900&display=swap">
<style>
  :root {
    --bg: #e9e7e4;
    --card-black: #0b0b0c;
    --card-sheen: #232325;
    --red: #e0262c;
    --red-dark: #a3161b;
    --white: #f4f4f4;
    --gray: #b9b9bb;
  }
  * { box-sizing: border-box; margin: 0; padding: 0; }
  html, body {
    width: 1200px; height: 1023px; overflow: hidden;
    background: var(--bg);
    font-family: "Lato", Arial, sans-serif;
  }
  .stage {
    position: relative; width: 1200px; height: 1023px;
    display: flex; flex-direction: column; align-items: center; justify-content: center; gap: 52px;
  }
  .card {
    position: relative; width: 760px; height: 434px;
    border-radius: 14px; overflow: hidden;
    background: linear-gradient(140deg, var(--card-sheen) 0%, var(--card-black) 45%, #000 100%);
    box-shadow: 0 10px 26px rgba(0,0,0,.25);
  }
  .card-art { position: absolute; inset: 0; }
  .identity { position: absolute; left: 70px; top: 170px; color: var(--white); }
  .identity__name { font-weight: 700; font-size: 30px; letter-spacing: .3px; }
  .identity__title { font-weight: 400; font-size: 20px; color: var(--red); margin-top: 4px; }
  .contacts { list-style: none; margin-top: 16px; }
  .contacts__item {
    display: flex; align-items: center; gap: 12px;
    font-size: 17px; color: var(--white); line-height: 27px;
  }
  .contacts__icon { width: 16px; height: 16px; flex: none; }
  .address { margin-top: 14px; color: var(--red); font-weight: 700; font-size: 19px; line-height: 24px; }
  .brand {
    position: absolute; display: flex; align-items: center; gap: 14px;
    color: var(--white); font-weight: 900; text-transform: uppercase;
  }
  .brand__mark { background: var(--red); flex: none; }
  .brand--front { right: 52px; top: 58px; font-size: 19px; line-height: 21px; }
  .brand--front .brand__mark { width: 30px; height: 30px; }
  .brand--back { left: 50%; top: 50%; transform: translate(-50%,-50%); font-size: 30px; line-height: 33px; gap: 20px; }
  .brand--back .brand__mark { width: 48px; height: 48px; }
</style>
</head>
<body>
<main class="stage">

  <section class="card card--front" aria-label="Business card front">
    <svg class="card-art" viewBox="0 0 760 434" aria-hidden="true">
      <path d="M0 56 H44 Q58 56 58 70 V150 Q58 164 44 164 H0 Z" fill="var(--red)"/>
      <path d="M0 150 H44 Q58 150 58 164 H0 Z" fill="var(--red-dark)"/>
      <line x1="380" y1="160" x2="640" y2="250" stroke="var(--red)" stroke-width="1.5"/>
    </svg>

    <div class="brand brand--front">
      <span class="brand__mark"></span>
      <span>Harwell<br>Industrial<br>Group</span>
    </div>

    <div class="identity">
      <h1 class="identity__name">Tom Harwell</h1>
      <p class="identity__title">Managing Director</p>
      <ul class="contacts">
        <li class="contacts__item">
          <svg class="contacts__icon" viewBox="0 0 16 16"><path d="M4 1 L6.5 4.5 5 6.5 Q6.5 9.5 9.5 11 L11.5 9.5 15 12 13 15 Q6 14 1 3 Z" fill="var(--red)"/></svg>
          0497 551 832
        </li>
        <li class="contacts__item">
          <svg class="contacts__icon" viewBox="0 0 16 16"><rect x="1" y="3" width="14" height="10" rx="1.5" fill="var(--red)"/><path d="M1.5 4 L8 9 14.5 4" stroke="#000" stroke-width="1.3" fill="none"/></svg>
          tomwork@vandilo.com.au
        </li>
        <li class="contacts__item">
          <svg class="contacts__icon" viewBox="0 0 16 16"><circle cx="8" cy="8" r="6.5" fill="none" stroke="var(--red)" stroke-width="1.6"/><path d="M1.5 8 H14.5 M8 1.5 Q4 8 8 14.5 M8 1.5 Q12 8 8 14.5" stroke="var(--red)" stroke-width="1.2" fill="none"/></svg>
          www.harwellindustrialgroup.com.au
        </li>
      </ul>
      <p class="address">417 Calloway Street,<br>Pembrook NSW 2458</p>
    </div>
  </section>

  <section class="card card--back" aria-label="Business card back">
    <svg class="card-art" viewBox="0 0 760 434" aria-hidden="true">
      <path d="M0 170 H44 Q58 170 58 184 V264 Q58 278 44 278 H0 Z" fill="var(--red)"/>
      <path d="M0 264 H44 Q58 264 58 278 H0 Z" fill="var(--red-dark)"/>
    </svg>
    <div class="brand brand--back">
      <span class="brand__mark"></span>
      <span>Harwell<br>Industrial<br>Group</span>
    </div>
  </section>

</main>
</body>
</html>
```